Law Firm Profile

I need a Law firm Profile design. Something professional, corporate inspired, unique and sophisticated. Preferred colours are blue, grey and white. Completion timeline is 5 days. Details of law firm are in the uploaded document

```html
<!DOCTYPE html>
<html lang="en">
<head>
<meta charset="utf-8">
<title>KSL Advocates – Law Firm Profile</title>
<link href="https://fonts.googleapis.com/css2?family=Cinzel:wght@400;700&family=Tinos:wght@400;700&display=swap" rel="stylesheet">
<style>
:root{
  --bg:#6e6e6e;
  --paper:#ffffff;
  --blue:#0b4ea6;
  --navy:#1f2c7c;
  --gold:#b9a42b;
  --ink:#333333;
  --grey:#eeeef0;
  --rule:#bdbdbd;
}
*{margin:0;padding:0;box-sizing:border-box}
html,body{width:997px;height:1200px;overflow:hidden;background:var(--bg)}
.canvas{position:relative;width:997px;height:1200px}
.page{position:absolute;width:386px;height:499px;background:var(--paper);overflow:hidden;font-family:"Tinos",serif;color:var(--ink)}
.page--cover{left:83px;top:80px}
.page--intro{left:531px;top:80px}
.page--people{left:80px;top:627px}
.page--structure{left:531px;top:627px}
.margin-pattern{position:absolute;left:0;top:0;width:24px;height:100%;background:linear-gradient(90deg,#f1f1f4,#fafafa)}
.abs{position:absolute}

/* cover */
.cover-title{left:67px;top:40px;font-family:"Cinzel",serif;color:var(--navy);line-height:1}
.cover-title .firm{font-size:23px;font-weight:400;letter-spacing:.5px}
.cover-title .doc{font-size:24px;font-weight:700;margin-top:6px}
.cover-grey{left:0;top:140px;width:386px;height:359px;background:var(--grey)}
.cover-photo{left:0;top:150px;width:386px;height:234px;background:linear-gradient(135deg,#6a6c74 0%,#4a4d55 45%,#7d6a55 75%,#5a4636 100%)}
.cover-tagline{left:66px;top:434px;font-family:"Cinzel",serif;font-size:14.5px;line-height:19px;color:#333;letter-spacing:.4px}

/* intro */
.intro-band{left:0;top:0;width:386px;height:116px;background:var(--blue)}
.intro-lead{left:35px;top:34px;width:317px;color:#fff;font-size:9.4px;line-height:12px;text-align:justify}
.gold-bar{background:var(--gold);height:4px}
.practice{left:35px;width:317px;font-size:6px;line-height:9.4px;text-align:justify}
.practice p{margin-bottom:13px}
.practice b{font-weight:700}
.footer{position:absolute;left:35px;top:471px;width:317px}
.footer-rule{height:1px;background:var(--rule);margin-right:6px}
.footer-dot{position:absolute;right:0;top:-3px;width:7px;height:7px;border-radius:50%;background:#9a9a9a}
.footer-text{font-size:3.6px;color:#888;margin-top:6px;letter-spacing:.2px}

/* people */
.handshake{left:35px;top:133px;width:317px;height:96px;background:linear-gradient(120deg,#3b4048 0%,#5d6168 50%,#8f8f93 100%)}
.personnel-box{left:35px;top:229px;width:317px;height:52px;background:var(--blue);color:#fff;font-family:"Cinzel",serif}
.personnel-box .label{position:absolute;left:19px;top:13px;font-size:11px;letter-spacing:.4px}
.personnel-box .name{position:absolute;left:19px;top:27px;font-size:11.5px;font-weight:700}
.bio{left:35px;width:317px;font-size:6px;line-height:9.4px;text-align:justify}
.heading{font-family:"Cinzel",serif;color:var(--blue);font-weight:400}
.associate-title{left:35px;top:389px;font-size:12px}

/* structure */
.section-title{left:35px;font-size:12.5px}
.roles{left:35px;list-style:none;font-size:8px;color:var(--blue);line-height:12.7px}
.roles li{display:flex;align-items:center;gap:5px}
.roles svg{width:7px;height:7px}
.support-label{left:46px;top:152px;font-size:8px;font-weight:700;color:#333;letter-spacing:.3px}
.gavel-photo{left:189px;top:99px;width:162px;height:125px;background:linear-gradient(135deg,#cfc6ba 0%,#9a7a5a 50%,#5b3a2a 75%,#d8cbb6 100%)}
.contact-box{left:35px;top:323px;width:317px;height:52px;background:var(--blue);color:#fff;font-family:"Cinzel",serif;font-size:12px;line-height:14px;padding:12px 0 0 20px;letter-spacing:.4px}
.contact{font-size:6.4px;line-height:11px;color:#333}
.contact .row{display:flex;align-items:center;gap:6px}
.contact svg{width:7px;height:7px;flex:none}
.brand-name{left:274px;top:392px;font-family:"Cinzel",serif;font-size:13px;line-height:16px;color:var(--blue)}
</style>
</head>
<body>
<div class="canvas">

  <!-- Page 1: cover -->
  <section class="page page--cover">
    <div class="abs cover-grey"></div>
    <div class="margin-pattern" role="img" aria-label="Faint geometric pattern along the left margin"></div>
    <svg class="abs" style="left:0;top:0" width="386" height="499" viewBox="0 0 386 499" aria-hidden="true">
      <rect x="0" y="0" width="386" height="140" fill="#fff"/>
      <polygon points="0,0 24,0 24,140 0,140" fill="#f4f4f6"/>
      <polygon points="237,120 386,120 386,150 225,150" fill="var(--blue)"/>
      <polygon points="385,384 385,499 342,499 311,413" fill="#fff"/>
      <polygon points="160,384 386,384 386,414 145,414" fill="var(--blue)"/>
    </svg>
    <div class="abs cover-photo" role="img" aria-label="Photo of a lawyer in a suit writing in a book beside a gavel and scales of justice"></div>
    <h1 class="abs cover-title"><div class="firm">KSL ADVOCATES</div><div class="doc">LAW FIRM PROFILE</div></h1>
    <p class="abs cover-tagline">ESTABLISHED LEGAL FIRM<br>SITUATED IN LUSAKA, ZAMBIA</p>
  </section>

  <!-- Page 2: introduction and practice areas -->
  <section class="page page--intro">
    <div class="margin-pattern" role="img" aria-label="Faint geometric pattern along the left margin"></div>
    <div class="abs intro-band"></div>
    <p class="abs intro-lead">KSL Advocates is an established legal firm situated in Lusaka, Zambia. The firm was founded in 2013 by Mr Daniel K Mwale S. C, the current Director of Public Prosecutions. The firm represents a wide range of clients both local and international and is dedicated to providing the highest quality of services in various areas of the law including –</p>
    <div class="abs gold-bar" style="left:35px;top:116px;width:135px"></div>
    <div class="abs practice" style="top:133px">
      <p><b>Corporate Law:</b> We provide comprehensive legal services for corporate clients including in the areas of corporate governance, regulatory compliance, due diligence and risk management advisory. We seamlessly manage the legal aspects of our clients’ transactions and ensure that all documentary and contractual requirements are professionally and strategically executed;</p>
      <p><b>Commercial Law:</b> We have vast knowledge and experience in navigating complex commercial legal matters, including contract drafting, negotiations and compliance. We are aligned with the international environment and our lawyers keep up to date on evolving rules of international law and any applicable conflict of laws issues. Our lawyers understand the interplay between the evolving digitalization of the business environment, jurisdictional variances and the legal implications of innovations to the legal environment ;</p>
      <p><b>Estate and Family Law:</b> We are well versed in handling estate planning, Wills, Trusts, guardianship, divorce and probate matters to address clients’ specific legal needs. Our flexible approach in implementing the full range of established dispute resolution methods at appropriate stages of the transactions and matters speaks to the successful management of even the most complex cases;</p>
      <p><b>Debt Collection:</b> We efficiently handle the recovery process which is crucial for the businesses, financial institutions and individuals we represent, ensuring that disruptions and cost to our clients are mitigated;</p>
      <p><b>Civil and Criminal Litigation;</b> We have a notable and well respected track record in the area of litigation and all ancillary processes, we have handled major cases in commercial, criminal, constitutional and other areas of the law. We are committed to ensuring that our work is backed by meticulous legal analysis, structure and sound strategy, ensuring that we draw from the benefits of the integrated and multi-faceted nature of our practice to ensure best results for our clients;</p>
      <p><b>Administrative Law:</b> We represent a significant number of clients in the area of public law and have handled a large number of judicial review matters regarding immigration and deportation matters, regulatory infringements among others. We are committed to offering comprehensive guidance, clear communication and swift and appropriate response and high quality strategy from the administrative stage, at first instance, and across all stages of the appeal process.</p>
    </div>
    <div class="footer"><div class="footer-rule"></div><div class="footer-dot"></div><div class="footer-text">KSL ADVOCATES LAW FIRM PROFILE</div></div>
  </section>

  <!-- Page 3: practice areas and key personnel -->
  <section class="page page--people">
    <div class="margin-pattern" role="img" aria-label="Faint geometric pattern along the left margin"></div>
    <div class="abs practice" style="top:35px">
      <p style="margin-bottom:12px"><b>Land Law:</b> We have handled a wide range of land matters including trespass litigation, encroachment, rectifications and conveyancing and manage a substantial caseload of cases.</p>
      <p><b>Constitutional Law:</b> We are a leading firm in constitutional law matters and have handled a plethora of presidential, parliamentary and local government election petitions. Our vast expertise in constitutional law is also displayed by our extensive portfolio in handling all manner of novel challenging matters in this area from constitutional interpretation to general constitutional petitions as well as motions. We have a strong database of case-law records and material which enhances our nuanced and detailed understanding of constitutional law enabling us to render well researched legal opinions to our clients.</p>
    </div>
    <div class="abs handshake" role="img" aria-label="Photo of two people shaking hands across a desk"></div>
    <div class="abs personnel-box">
      <span class="label">KEY PERSONNEL</span>
      <span class="name">MANAGING PARTNER – NATASHA CHILESHE</span>
    </div>
    <div class="abs gold-bar" style="left:53px;top:281px;width:97px"></div>
    <p class="abs bio" style="top:296px"><b>Natasha Chileshe</b> has more than seven years of experience in various areas of the law including commercial law, mining law, construction law, labour law, company law, constitutional law, human rights law, ICT law, administrative law, legislative drafting, civil and criminal litigation and energy law. She studied law at Kabulonga University, graduated in 2015 and was admitted to the bar in 2016. Since April 2022 She has sat on the licensing committee of the Energy Licensing Board and is well versed in the matters relating to the energy sector. She is a member of the Press Freedom Trust and advocates for digital rights and freedom of expression. She provides legal advisory services to various civil society organizations and undertakes strategic litigation and she holds a postgraduate diploma in legislative drafting and advocates for legislative reform and advancement in various areas of the law.</p>
    <h2 class="abs heading associate-title">ASSOCIATE – RUTH BANDA</h2>
    <p class="abs bio" style="top:408px">Ruth Banda has over three years of experience in civil litigation, conveyancing, handling corporate and commercial transactions, contract drafting, family law, human rights law , labour disputes, debt recovery as well as administrative law. She studied at Copperbelt Distance University and graduated in 2016 and was admitted to the Bar in 2020. She is a member of the Public Interest Committee of the Zambia Bar Society and has a keen interest in human rights matters.</p>
    <div class="footer"><div class="footer-rule"></div><div class="footer-dot"></div><div class="footer-text">KSL ADVOCATES LAW FIRM PROFILE</div></div>
  </section>

  <!-- Page 4: structure, values and contact -->
  <section class="page page--structure">
    <div class="margin-pattern" role="img" aria-label="Faint geometric pattern along the left margin"></div>
    <h2 class="abs heading section-title" style="top:35px">MANAGEMENT STRUCTURE</h2>
    <p class="abs bio" style="top:54px">We have a dedicated team of personnel whose primary goal is to provide the highest quality of service in compliance with all applicable rules of professional conduct. Our support team is friendly, skilled and diverse and work together to ensure that the lawyer-client relationship is seamlessly and properly managed.</p>
    <ul class="abs roles" style="top:104px">
      <li><svg viewBox="0 0 10 10"><circle cx="5" cy="5" r="4.3" fill="none" stroke="#555" stroke-width="1"/><path d="M3 5.2 4.5 6.6 7.2 3.6" fill="none" stroke="#555" stroke-width="1"/></svg>MANAGING PARTNER</li>
      <li><svg viewBox="0 0 10 10"><circle cx="5" cy="5" r="4.3" fill="none" stroke="#555" stroke-width="1"/><path d="M3 5.2 4.5 6.6 7.2 3.6" fill="none" stroke="#555" stroke-width="1"/></svg>PARTNER (S)</li>
      <li><svg viewBox="0 0 10 10"><circle cx="5" cy="5" r="4.3" fill="none" stroke="#555" stroke-width="1"/><path d="M3 5.2 4.5 6.6 7.2 3.6" fill="none" stroke="#555" stroke-width="1"/></svg>ASSOCIATE (S)</li>
    </ul>
    <p class="abs support-label">SUPPORT STAFF:</p>
    <ul class="abs roles" style="top:164px">
      <li><svg viewBox="0 0 10 10"><circle cx="5" cy="5" r="4.3" fill="none" stroke="#555" stroke-width="1"/><path d="M3 5.2 4.5 6.6 7.2 3.6" fill="none" stroke="#555" stroke-width="1"/></svg>OFFICE MANAGER</li>
      <li><svg viewBox="0 0 10 10"><circle cx="5" cy="5" r="4.3" fill="none" stroke="#555" stroke-width="1"/><path d="M3 5.2 4.5 6.6 7.2 3.6" fill="none" stroke="#555" stroke-width="1"/></svg>ASSISTANT OFFICE MANAGER</li>
      <li><svg viewBox="0 0 10 10"><circle cx="5" cy="5" r="4.3" fill="none" stroke="#555" stroke-width="1"/><path d="M3 5.2 4.5 6.6 7.2 3.6" fill="none" stroke="#555" stroke-width="1"/></svg>LEGAL CLERK</li>
      <li><svg viewBox="0 0 10 10"><circle cx="5" cy="5" r="4.3" fill="none" stroke="#555" stroke-width="1"/><path d="M3 5.2 4.5 6.6 7.2 3.6" fill="none" stroke="#555" stroke-width="1"/></svg>RECEPTIONIST</li>
    </ul>
    <div class="abs gavel-photo" role="img" aria-label="Photo of a wooden gavel with brass band beside scales of justice"></div>
    <h2 class="abs heading section-title" style="top:239px">CORE VALUES</h2>
    <p class="abs bio" style="top:258px">We take pride in the quality of our legal services in which we incorporate our core values which include integrity, passion, credibility, continuous professional development and excellent client care in the management of our clients’ instructions. The firm is regulated by the Zambia Bar Society and adherence to legal ethics and conduct forms the backbone of our practice and the firm’s culture. We also aim to efficiently to harness creative, bespoke and expert solutions to meet every client’s particular needs.</p>
    <div class="abs contact-box">BUSINESS ADDRESS<br>AND CONTACT INFORMATION</div>
    <div class="abs gold-bar" style="left:54px;top:375px;width:96px"></div>
    <div class="abs contact" style="left:42px;top:393px">
      <div class="row" style="align-items:flex-start;line-height:9px"><svg viewBox="0 0 10 10"><path d="M5 .5a3.3 3.3 0 0 0-3.3 3.3C1.7 6.3 5 9.5 5 9.5s3.3-3.2 3.3-5.7A3.3 3.3 0 0 0 5 .5Zm0 4.6a1.3 1.3 0 1 1 0-2.6 1.3 1.3 0 0 1 0 2.6Z" fill="var(--blue)"/></svg><span>Plot No. 14, Kafue Road, Rhodes Park<br>P.O. Box 41027, Woodlands, Lusaka, Zambia</span></div>
    </div>
    <div class="abs contact" style="left:42px;top:416px">
      <div class="row"><svg viewBox="0 0 10 10"><path d="M2.2 1 3.8 2.6 2.9 3.8c.6 1.3 1.9 2.6 3.3 3.3l1.2-.9L9 7.8 7.9 9C4.5 8.6 1.4 5.5 1 2.1Z" fill="none" stroke="var(--blue)" stroke-width=".9"/></svg>+260 7700 12345</div>
      <div class="row"><svg viewBox="0 0 10 10"><path d="M2.2 1 3.8 2.6 2.9 3.8c.6 1.3 1.9 2.6 3.3 3.3l1.2-.9L9 7.8 7.9 9C4.5 8.6 1.4 5.5 1 2.1Z" fill="none" stroke="var(--blue)" stroke-width=".9"/></svg>+260 9600 23456</div>
      <div class="row"><svg viewBox="0 0 10 10"><path d="M2.2 1 3.8 2.6 2.9 3.8c.6 1.3 1.9 2.6 3.3 3.3l1.2-.9L9 7.8 7.9 9C4.5 8.6 1.4 5.5 1 2.1Z" fill="none" stroke="var(--blue)" stroke-width=".9"/></svg>+260 9700 34567</div>
      <div class="row"><svg viewBox="0 0 10 10"><path d="M2.2 1 3.8 2.6 2.9 3.8c.6 1.3 1.9 2.6 3.3 3.3l1.2-.9L9 7.8 7.9 9C4.5 8.6 1.4 5.5 1 2.1Z" fill="none" stroke="var(--blue)" stroke-width=".9"/></svg>+260 7600 45678</div>
    </div>
    <div class="abs contact" style="left:152px;top:438px">
      <div class="row"><svg viewBox="0 0 10 10"><path d="M2.2 1 3.8 2.6 2.9 3.8c.6 1.3 1.9 2.6 3.3 3.3l1.2-.9L9 7.8 7.9 9C4.5 8.6 1.4 5.5 1 2.1Z" fill="none" stroke="var(--blue)" stroke-width=".9"/></svg>+260 211000111</div>
      <div class="row"><svg viewBox="0 0 10 10"><rect x="1" y="2.2" width="8" height="5.6" fill="none" stroke="var(--blue)" stroke-width=".9"/><path d="M1 2.4 5 5.6 9 2.4" fill="none" stroke="var(--blue)" stroke-width=".9"/></svg>info@ksladvocates.example</div>
    </div>
    <p class="abs brand-name">KSL<br>ADVOCATES</p>
    <div class="footer"><div class="footer-rule"></div><div class="footer-dot"></div><div class="footer-text">KSL ADVOCATES LAW FIRM PROFILE</div></div>
  </section>

</div>
</body>
</html>
```